Business Card Design Project

A new design for our business cards for a small casting/talent agency, we would like to incorporate the logo and brand colors within the design, below are the information that should be on the card

(Name)
(Title)

Corvane Reels FZ-LLC
Harlow Studio Park
Building 7, Suite 418
Dubai, UAE
PO Box 681247
+97143810579
info@CorvaneReels.com

Target Market(s)

production companies, film makers, media, entertainment industry

Industry/Entity Type

Business

Requirements
Must have
• logo, logo colors
Nice to have
• cutting edge design, sleek and modern
Should not have
• playful, funky, congested

```html
<!DOCTYPE html>
<html lang="en">
<head>
<meta charset="utf-8">
<title>Corvane Reels – Business Card</title>
<link rel="stylesheet" href="https://fonts.googleapis.com/css2?family=Open+Sans:wght@400;600;700&display=swap">
<style>
  :root {
    --backdrop: #2a2a2c;
    --card-navy: #1d2f5e;
    --card-navy-deep: #182851;
    --ink-light: #d6dbe3;
    --ink-white: #ffffff;
    --mark-grey: #aab2bd;
    --rule: #8d99b3;
  }
  * { box-sizing: border-box; margin: 0; padding: 0; }
  html, body {
    width: 1200px; height: 900px; overflow: hidden;
    background: var(--backdrop);
    font-family: "Open Sans", Arial, sans-serif;
  }
  .stage { position: relative; width: 1200px; height: 900px; }

  .card {
    position: absolute;
    width: 560px; height: 320px;
    background: var(--card-navy);
    box-shadow: 0 14px 30px rgba(0,0,0,.55);
  }
  .card--front { left: 220px; top: 110px; }
  .card--back  { left: 420px; top: 470px; }

  /* Front: brand lockup */
  .brand-lockup {
    position: absolute; left: 50%; top: 50%;
    width: 200px; height: 200px; margin: -100px 0 0 -100px;
    border-radius: 50%;
    background: var(--card-navy-deep);
    border: 3px solid var(--ink-light);
    display: flex; align-items: center; justify-content: center;
  }
  .brand-name {
    font-weight: 600; font-size: 28px; color: var(--ink-light);
    text-align: center; line-height: 1.1;
  }

  /* Back: contact details */
  .holder { position: absolute; left: 40px; top: 52px; }
  .holder-name {
    font-weight: 700; font-size: 21px; letter-spacing: .5px;
    color: var(--ink-light); text-transform: uppercase;
  }
  .holder-title { font-size: 12px; color: var(--ink-light); margin-top: -2px; }

  .details {
    position: absolute; left: 58px;
    border-left: 1px solid var(--rule);
    padding-left: 12px;
    color: var(--ink-light); font-size: 13px; line-height: 1.35;
  }
  .details--address { top: 118px; }
  .details--contact { top: 232px; }
  .company { font-weight: 700; }
  .gap { margin-top: 8px; }

  .brand-mark-large {
    position: absolute; right: 36px; top: 40px;
    width: 230px; height: 230px; border-radius: 50%;
    background: var(--mark-grey);
    display: flex; align-items: center; justify-content: center;
  }
  .brand-mark-large .brand-name { color: var(--ink-white); font-size: 30px; }
</style>
</head>
<body>
<main class="stage">
  <section class="card card--front" aria-label="Card front">
    <div class="brand-lockup">
      <span class="brand-name">Corvane<br>Reels</span>
    </div>
  </section>

  <section class="card card--back" aria-label="Card back">
    <div class="holder">
      <h1 class="holder-name">Maren Holloway</h1>
      <p class="holder-title">General Manager</p>
    </div>

    <address class="details details--address">
      <span class="company">Corvane Reels FZ-LLC</span><br>
      Harlow Studio Park<br>
      <span class="gap" style="display:inline-block">Building 7, Suite 418</span><br>
      Dubai, UAE<br>
      PO Box 681247
    </address>

    <address class="details details--contact">
      +97143810579<br>
      info@CorvaneReels.com<br>
      www.CorvaneReels.com
    </address>

    <div class="brand-mark-large">
      <span class="brand-name">Corvane<br>Reels</span>
    </div>
  </section>
</main>
</body>
</html>
```